GridMonarch : This is a Puzzle and This is not a Puzzle

GridMonarch is a new addictive way to play Sudoku (see description on the attached document).
We would like your help in developing a design for the playscreen of the game (a mock-up is in the attached document)
The winner will be entrusted with the work of the complete design of the application (home screen, configuration screen, etc.) in a specific contract.
Thank you from Paris France.
Best.
Bertrand

```html
<!DOCTYPE html>
<html lang="en">
<head>
<meta charset="utf-8">
<title>GridMonarch – Play Screen</title>
<link rel="stylesheet" href="https://fonts.googleapis.com/css2?family=Source+Sans+3:wght@400;600&family=Arimo:wght@400;700&display=swap">
<style>
:root{
  --bg:#ffffff;
  --ink:#000000;
  --navy:#0000c8;
  --cyan:#00f0ff;
  --c-gray:#c0c0c0;
  --c-yellow:#ffff00;
  --c-lemon:#fff01f;
  --c-blue:#0000bb;
  --c-black:#000000;
  --c-magenta:#ff00ff;
  --c-red:#ff0000;
  --c-cyan:#00ffff;
  --c-green:#00ee00;
  --c-lime:#22ff22;
  --c-gold:#cc9900;
  --c-orange:#ffaa00;
  --line:#9a9a9a;
}
*{box-sizing:border-box;margin:0;padding:0}
html,body{width:1200px;height:617px;overflow:hidden;background:var(--bg)}
body{position:relative;font-family:"Source Sans 3",sans-serif}

.toggle{position:absolute;left:63px;width:237px;height:53px;border-radius:27px;display:flex;align-items:center;padding-left:8px}
.toggle--level{top:79px;background:var(--navy)}
.toggle--help{top:143px;background:var(--cyan)}
.toggle__knob{width:38px;height:38px;border-radius:50%;background:#fff;margin-right:14px}
.toggle svg{display:block}

.tool{position:absolute;width:43px;height:43px;border-radius:50%;background:#fff;box-shadow:0 2px 8px rgba(0,0,0,.14);display:flex;align-items:center;justify-content:center;transform:translate(-50%,-50%)}
.tool svg{width:20px;height:20px}
.tool__label{font-family:"Arimo",sans-serif;font-size:14px;text-decoration:underline;color:#333}

.palette{position:absolute;left:346px;top:79px;width:45px}
.palette__swatch{height:49.2px;position:relative}
.badge{position:absolute;width:13px;height:13px;background:var(--ink);color:#fff;font-family:"Arimo",sans-serif;font-weight:700;font-size:10px;line-height:13px;text-align:center}
.palette .badge{left:-9px;bottom:2px}

.board{position:absolute;left:428px;top:79px;width:443px;height:443px;display:grid;grid-template-columns:repeat(9,1fr);grid-template-rows:repeat(9,1fr);border:2px solid var(--ink);background:var(--bg)}
.cell{border-right:1px solid var(--line);border-bottom:1px solid var(--line);display:flex;align-items:center;justify-content:center;font-size:33px;font-weight:600;color:var(--ink);line-height:1}
.cell:nth-child(9n){border-right:none}
.cell:nth-last-child(-n+9){border-bottom:none}
.cell--light{color:#fff}

.numbers{position:absolute;left:908px;top:79px;width:49px;border:1px solid var(--line)}
.numbers__key{height:49.2px;border-bottom:1px solid var(--line);font-family:"Arimo",sans-serif;font-size:22px;display:flex;align-items:center;justify-content:center;position:relative}
.numbers__key:last-child{border-bottom:none}
.numbers .badge{right:-22px;bottom:2px}
</style>
</head>
<body>

<div class="toggle toggle--level">
  <span class="toggle__knob"></span>
  <svg width="150" height="26" viewBox="0 0 150 26" aria-label="Level four of five">
    <g fill="#fff" stroke="#fff" stroke-width="1.5" stroke-linejoin="round">
      <path id="star" d="M13 2l3.3 7 7.5.8-5.6 5.1 1.6 7.4L13 18.5 6.2 22.3l1.6-7.4L2.2 9.8l7.5-.8z"/>
      <use href="#star" x="30"/><use href="#star" x="60"/><use href="#star" x="90"/>
      <use href="#star" x="120" fill="none"/>
    </g>
  </svg>
</div>
<div class="toggle toggle--help">
  <span class="toggle__knob"></span>
  <svg width="150" height="26" viewBox="0 0 150 26" aria-label="Help three of five">
    <g fill="#0000c8" stroke="#0000c8" stroke-width="1.5" stroke-linejoin="round">
      <use href="#star"/><use href="#star" x="30"/><use href="#star" x="60"/>
      <use href="#star" x="90" fill="none"/><use href="#star" x="120" fill="none"/>
    </g>
  </svg>
</div>

<svg width="0" height="0" style="position:absolute">
  <defs>
    <g id="i-rewind"><path d="M11 4v12L3 10zM19 4v12l-8-6z" fill="#000"/></g>
    <g id="i-grid" fill="#000"><rect x="2" y="2" width="4.5" height="4.5"/><rect x="7.8" y="2" width="4.5" height="4.5"/><rect x="13.6" y="2" width="4.5" height="4.5"/><rect x="2" y="7.8" width="4.5" height="4.5"/><rect x="7.8" y="7.8" width="4.5" height="4.5"/><rect x="13.6" y="7.8" width="4.5" height="4.5"/><rect x="2" y="13.6" width="4.5" height="4.5"/><rect x="7.8" y="13.6" width="4.5" height="4.5"/><rect x="13.6" y="13.6" width="4.5" height="4.5"/></g>
    <g id="i-eraser"><path d="M12 3l6 6-7 7H6l-3-3z" fill="#000"/><path d="M6 16l-3-3 4-4 6 6-1 1z" fill="#fff" stroke="#000" stroke-width="1.2"/><path d="M2 18h16" stroke="#000" stroke-width="1.2"/></g>
    <g id="i-bulb" fill="#000"><path d="M10 5a5 5 0 0 0-3 9v2h6v-2a5 5 0 0 0-3-9z"/><rect x="7.5" y="16.8" width="5" height="1.6"/><path d="M10 0v3M3 3l2 2M17 3l-2 2M0 9h3M17 9h3" stroke="#000" stroke-width="1.2"/></g>
    <g id="i-home"><path d="M10 2L1 10h3v8h4v-5h4v5h4v-8h3z" fill="#000"/></g>
  </defs>
</svg>

<div class="tool" style="left:182px;top:290px"><svg viewBox="0 0 20 20"><use href="#i-rewind"/></svg></div>
<div class="tool" style="left:182px;top:360px"><svg viewBox="0 0 20 20"><use href="#i-grid"/></svg></div>
<div class="tool" style="left:182px;top:430px"><svg viewBox="0 0 20 20"><use href="#i-eraser"/></svg></div>
<div class="tool" style="left:182px;top:499px"><svg viewBox="0 0 20 20"><use href="#i-bulb"/></svg></div>

<div class="palette">
  <div class="palette__swatch" style="background:var(--c-lemon)"><span class="badge">4</span></div>
  <div class="palette__swatch" style="background:var(--c-magenta)"><span class="badge">6</span></div>
  <div class="palette__swatch" style="background:var(--c-gold)"><span class="badge">6</span></div>
  <div class="palette__swatch" style="background:var(--c-red)"><span class="badge">4</span></div>
  <div class="palette__swatch" style="background:var(--c-orange)"><span class="badge">8</span></div>
  <div class="palette__swatch" style="background:var(--c-blue)"><span class="badge">4</span></div>
  <div class="palette__swatch" style="background:var(--c-lime)"><span class="badge">5</span></div>
  <div class="palette__swatch" style="background:var(--c-cyan)"><span class="badge">7</span></div>
  <div class="palette__swatch" style="background:var(--c-black)"><span class="badge">3</span></div>
</div>

<div class="board">
  <!-- row 1 -->
  <div class="cell" style="background:var(--c-gray)">4</div><div class="cell"></div><div class="cell">3</div><div class="cell cell--light" style="background:var(--c-blue)">5</div><div class="cell cell--light" style="background:var(--c-black)">2</div><div class="cell"></div><div class="cell"></div><div class="cell" style="background:var(--c-magenta)">6</div><div class="cell" style="background:var(--c-yellow)"></div>
  <!-- row 2 -->
  <div class="cell" style="background:var(--c-yellow)">9</div><div class="cell" style="background:var(--c-blue)"></div><div class="cell"></div><div class="cell">7</div><div class="cell" style="background:var(--c-red)">1</div><div class="cell"></div><div class="cell cell--light" style="background:var(--c-black)">3</div><div class="cell" style="background:var(--c-cyan)">5</div><div class="cell">4</div>
  <!-- row 3 -->
  <div class="cell cell--light" style="background:var(--c-black)">1</div><div class="cell"></div><div class="cell" style="background:var(--c-green)"></div><div class="cell">6</div><div class="cell"></div><div class="cell">4</div><div class="cell"></div><div class="cell"></div><div class="cell" style="background:var(--c-gray)">9</div>
  <!-- row 4 -->
  <div class="cell">7</div><div class="cell">1</div><div class="cell"></div><div class="cell" style="background:var(--c-green)">3</div><div class="cell"></div><div class="cell" style="background:var(--c-red)">5</div><div class="cell"></div><div class="cell" style="background:var(--c-gray)"></div><div class="cell" style="background:var(--c-gold)">6</div>
  <!-- row 5 -->
  <div class="cell">5</div><div class="cell"></div><div class="cell">9</div><div class="cell" style="background:var(--c-yellow)">2</div><div class="cell" style="background:var(--c-blue)"></div><div class="cell cell--light" style="background:var(--c-black)">6</div><div class="cell"></div><div class="cell"></div><div class="cell" style="background:var(--c-red)">8</div>
  <!-- row 6 -->
  <div class="cell"></div><div class="cell" style="background:var(--c-green)">2</div><div class="cell"></div><div class="cell" style="background:var(--c-gold)"></div><div class="cell" style="background:var(--c-cyan)"></div><div class="cell"></div><div class="cell" style="background:var(--c-yellow)">5</div><div class="cell cell--light" style="background:var(--c-black)">7</div><div class="cell" style="background:var(--c-magenta)">3</div>
  <!-- row 7 -->
  <div class="cell"></div><div class="cell"></div><div class="cell"></div><div class="cell"></div><div class="cell" style="background:var(--c-gray)">6</div><div class="cell" style="background:var(--c-blue)"></div><div class="cell"></div><div class="cell" style="background:var(--c-yellow)">3</div><div class="cell"></div>
  <!-- row 8 -->
  <div class="cell"></div><div class="cell" style="background:var(--c-red)"></div><div class="cell">5</div><div class="cell"></div><div class="cell"></div><div class="cell"></div><div class="cell"></div><div class="cell" style="background:var(--c-gold)">4</div><div class="cell"></div>
  <!-- row 9 -->
  <div class="cell cell--light" style="background:var(--c-blue)">3</div><div class="cell cell--light" style="background:var(--c-black)">4</div><div class="cell"></div><div class="cell" style="background:var(--c-magenta)"></div><div class="cell" style="background:var(--c-green)">5</div><div class="cell" style="background:var(--c-gold)">7</div><div class="cell" style="background:var(--c-gray)">8</div><div class="cell" style="background:var(--c-red)">9</div><div class="cell"></div>
</div>

<div class="numbers">
  <div class="numbers__key">1<span class="badge">7</span></div>
  <div class="numbers__key">2<span class="badge">6</span></div>
  <div class="numbers__key">3<span class="badge">4</span></div>
  <div class="numbers__key">4<span class="badge">5</span></div>
  <div class="numbers__key">5<span class="badge">4</span></div>
  <div class="numbers__key">6<span class="badge">3</span></div>
  <div class="numbers__key">7<span class="badge">5</span></div>
  <div class="numbers__key">8<span class="badge">8</span></div>
  <div class="numbers__key">9<span class="badge">6</span></div>
</div>

<div class="tool" style="left:1063px;top:106px"><svg viewBox="0 0 20 20"><use href="#i-home"/></svg></div>
<div class="tool" style="left:1063px;top:184px"><span class="tool__label">60"</span></div>
<div class="tool" style="left:1063px;top:263px"><svg viewBox="0 0 20 20"><use href="#i-rewind"/></svg></div>
<div class="tool" style="left:1063px;top:342px"><svg viewBox="0 0 20 20"><use href="#i-grid"/></svg></div>
<div class="tool" style="left:1063px;top:421px"><svg viewBox="0 0 20 20"><use href="#i-eraser"/></svg></div>
<div class="tool" style="left:1063px;top:500px"><svg viewBox="0 0 20 20"><use href="#i-bulb"/></svg></div>

</body>
</html>
```